Cover for a recovery from breast augmentation surgery pamphlet

Need a cover which includes my logo for new pamphlet on recovering from breast augmentation surgery It is just a quick how to guide.
I would like the cover to incorporate the Borela logo(2 options given) and be simple and clean. Will require in a vector file as well.

The title:
Well, Your Chest Is Upgraded...
WHAT NEXT?!

By: Borela

A little about me: I am an adult industry writer and am looking to do a mainstream project. This is a project I want to appeal to mainstream women.

Target Market(s)

Women who are recovering from or entertaining breast augmentation surgery

Font styles to use
Serif

Requirements
Must have
• One Borela logo, titile, and by Borela
Nice to have
• i love modern clean sleek design that is easy to read
Should not have
• nothing that would offend women or make them uncomfortable about their body

```html
<!DOCTYPE html>
<html lang="en">
<head>
<meta charset="utf-8">
<title>Well, Your Chest Is Upgraded... What Next?! — Pamphlet Cover</title>
<link rel="stylesheet" href="https://fonts.googleapis.com/css2?family=Cormorant+Garamond:wght@500;600&family=Oxygen:wght@400;700&display=swap">
<style>
  :root {
    --backdrop: #2a1911;
    --cover-light: #fffafb;
    --cover-mid: #f6dcdc;
    --cover-edge: #efbcbe;
    --ink: #1d1a1b;
    --accent-pink: #e04a9f;
    --brand-pink: #c13c93;
    --figure-deep: #eaa3bd;
    --figure-light: #fbe7ee;
  }
  * { box-sizing: border-box; margin: 0; padding: 0; }
  html, body {
    width: 1200px;
    height: 1200px;
    overflow: hidden;
    background: var(--backdrop);
  }
  .cover {
    position: absolute;
    left: 240px;
    top: 35px;
    width: 720px;
    height: 1130px;
    overflow: hidden;
    background: radial-gradient(ellipse 70% 60% at 45% 50%, var(--cover-light) 0%, var(--cover-mid) 55%, var(--cover-edge) 100%);
  }
  .cover__figure {
    position: absolute;
    left: 0;
    top: 124px;
    width: 346px;
    height: 960px;
    background: linear-gradient(180deg, var(--figure-light) 0%, var(--figure-deep) 45%, var(--figure-light) 75%, var(--figure-deep) 100%);
    opacity: 0.75;
    border-radius: 40% 60% 30% 30% / 12% 12% 6% 6%;
  }
  .title { position: absolute; left: 0; top: 0; width: 100%; }
  .title__lead {
    position: absolute;
    left: 360px;
    font-family: "Oxygen", sans-serif;
    font-weight: 400;
    font-size: 47px;
    line-height: 1;
    color: var(--ink);
    white-space: nowrap;
  }
  .title__lead--first { top: 172px; }
  .title__lead--second { top: 240px; }
  .title__accent {
    position: absolute;
    left: 312px;
    top: 300px;
    font-family: "Cormorant Garamond", serif;
    font-weight: 600;
    font-size: 74px;
    line-height: 1.05;
    color: var(--accent-pink);
    white-space: nowrap;
  }
  .title__question {
    position: absolute;
    left: 372px;
    top: 493px;
    font-family: "Oxygen", sans-serif;
    font-weight: 700;
    font-size: 46px;
    line-height: 1;
    color: #000;
    white-space: nowrap;
  }
  .brand {
    position: absolute;
    left: 360px;
    top: 870px;
    width: 210px;
    text-align: center;
    font-family: "Cormorant Garamond", serif;
    font-weight: 600;
    font-size: 72px;
    line-height: 1;
    color: var(--brand-pink);
  }
  .byline {
    position: absolute;
    left: 360px;
    top: 1026px;
    width: 210px;
    text-align: center;
    font-family: "Oxygen", sans-serif;
    font-weight: 400;
    font-size: 24px;
    color: #2c2a2b;
    white-space: nowrap;
  }
</style>
</head>
<body>
  <main class="cover">
    <div class="cover__figure" role="img" aria-label="Soft pink silhouette of a woman dancing on tiptoe with flowing hair"></div>

    <h1 class="title">
      <span class="title__lead title__lead--first">Well,</span>
      <span class="title__lead title__lead--second">Your Chest Is</span>
      <span class="title__accent" style="top:320px;">Upgraded...</span>
      <span class="title__question">WHAT NEXT?!</span>
    </h1>

    <div class="brand">Borela</div>
    <p class="byline">Author: Borela</p>
  </main>
</body>
</html>
```